Family Office for small businesses needs clear web site

I founded VORELTA Family Office, which is a french family office design to change the relationship between the customer and the wealth manager/insurance broker.
The main focus is : we give back to the client all the commissions / hidden costs we gain from the insurance companies / real estate builders and we bill to the client an annual fee proportional to the wealth. Thus a transparent relationship exempt from conflict of interest

I want a WORPRESS theme design that will be easily customizable in the future. Using and existing wordpress theme is not a problem, as long as i get to customize it in the future if necessary.
I want the web site to be Simple, clear, explaining the concepts detailed in the word doc i join to this project
In the chart are some of the things we do (not all, but most).
Also i joined some question a client might ask himself before calling us

i am available to clarify any issue or concepts
Updates

Target Market(s)

small businesses, specically their boss

Industry/Entity Type

Office

Number of Pages Required

1 page

Font styles to use
Serif

Colors
85acd3
3176b5
0455a3
cedeed
eaf1f7
cee9f5
85cae6
33a6d7
0692cd

Requirements
Must have
• I would like to have a one page wordpress theme personalized by a designer.
• I don't really care if you use an existing wordpress theme, as long as it can be upgraded/customized later on using wordpress/admin.
• I can even provide some themes I bought if it can help maintain the budget..
• O I can pay additional fee for a theme you bought to provide the design..

```html
<!DOCTYPE html>
<html lang="en">
<head>
<meta charset="utf-8">
<title>VORELTA Family Office</title>
<link href="https://fonts.googleapis.com/css2?family=Open+Sans:wght@300;400;600;700;800&display=swap" rel="stylesheet">
<style>
:root{
  --navy:#0a2f5c;
  --deep:#0455a3;
  --blue:#3176b5;
  --sky:#0692cd;
  --light:#85acd3;
  --pale:#cedeed;
  --mist:#eaf1f7;
  --text:#555f6b;
  --muted:#8a949f;
  --white:#ffffff;
}
*{margin:0;padding:0;box-sizing:border-box}
html,body{width:1200px;height:3836px;overflow:hidden}
body{font-family:"Open Sans",Arial,sans-serif;color:var(--text);background:var(--white);position:relative}
.section{position:absolute;left:0;width:1200px}
h2.section-title{font-size:26px;font-weight:600;color:var(--deep);text-align:center}
.lead{font-size:13px;line-height:22px;color:var(--muted);text-align:center}
.btn{display:inline-block;background:var(--sky);color:var(--white);font-size:13px;padding:12px 24px;border-radius:3px;text-decoration:none}
.btn-outline{display:inline-block;border:1px solid var(--white);color:var(--white);font-size:13px;padding:10px 22px;border-radius:3px}

/* header */
.site-header{top:0;height:88px;background:rgba(255,255,255,.95);z-index:3;display:flex;align-items:center;justify-content:space-between;padding:0 100px}
.brand{display:flex;align-items:center;gap:12px}
.brand-dot{width:26px;height:26px;border-radius:50%;background:var(--blue)}
.brand-name{font-size:24px;font-weight:600;color:var(--blue);letter-spacing:1px}
.main-nav{display:flex;gap:36px;font-size:12px;font-weight:600;color:#6b7580;letter-spacing:.5px}

/* hero */
.hero{top:0;height:592px;background:linear-gradient(100deg,#f3f6fa 0%,#e3eaf2 45%,#b9c6d3 70%,#8d9aa8 100%)}
.hero-text{position:absolute;left:100px;top:190px}
.hero-text h1{font-size:56px;font-weight:800;color:var(--deep);line-height:60px}
.hero-text .tagline{font-size:36px;font-weight:300;color:var(--blue);line-height:44px}
.hero-text p{font-size:16px;color:var(--sky);line-height:24px;margin:14px 0 26px;width:360px}
.hero-arrow{position:absolute;top:290px;width:30px;height:30px}

/* intro & services */
.intro{top:592px;height:590px}
.intro h2{margin-top:58px}
.intro .lead{width:1000px;margin:18px auto 0}
.services{position:absolute;left:100px;top:240px;width:1000px;display:grid;grid-template-columns:1fr 1fr;column-gap:80px;row-gap:48px}
.service{display:flex;gap:18px}
.service svg{flex:none}
.service h3{font-size:15px;font-weight:600;color:var(--deep);margin-bottom:8px}
.service p{font-size:12px;line-height:20px;color:var(--muted)}

/* council */
.council{top:1182px;height:520px}
.council h2{font-size:22px}
.cards{position:absolute;left:100px;top:82px;display:flex;gap:12px}
.card{position:relative;width:326px;height:355px}
.card-caption{position:absolute;left:0;bottom:22px;background:rgba(20,28,40,.85);color:var(--white);font-size:12px;font-weight:600;padding:10px 16px;max-width:240px;line-height:18px}
.dots{position:absolute;top:462px;left:0;width:1200px;display:flex;justify-content:center;gap:8px}
.dots span{width:8px;height:8px;border-radius:50%;background:var(--pale)}
.dots span.on{background:var(--blue)}

/* value */
.value{top:1712px;height:430px}
.value-photo{position:absolute;left:0;top:0;width:600px;height:430px;background:linear-gradient(120deg,#dfe6ee 0%,#b3c0ce 55%,#7f91a5 100%)}
.value-panel{position:absolute;left:600px;top:0;width:600px;height:430px;background:var(--deep);padding:56px 80px 0 80px;color:var(--white)}
.value-panel h2{font-size:26px;font-weight:600;margin-bottom:24px}
.value-panel p{font-size:12px;line-height:21px;color:#d6e4f3;margin-bottom:18px}

/* offer */
.offer{top:2142px;height:640px}
.offer h2{margin-top:90px}
.offer .lead{margin-top:14px}
.offer-list{position:absolute;left:100px;top:220px;width:1000px;display:flex;justify-content:space-between}
.offer-item{width:300px;text-align:center}
.offer-item svg{display:block;margin:0 auto 20px}
.offer-item h3{font-size:15px;font-weight:600;color:#333d48;margin-bottom:10px}
.offer-item p{font-size:12px;line-height:20px;color:var(--muted)}

/* about */
.about{top:2800px;height:370px;background:var(--mist)}
.about-text{position:absolute;left:100px;top:56px;width:420px}
.about-text h2{font-size:26px;font-weight:600;color:var(--deep);margin-bottom:18px}
.about-text p{font-size:12px;line-height:21px;color:var(--muted);margin-bottom:26px}
.about-photo{position:absolute;left:600px;top:0;width:600px;height:370px;background:linear-gradient(90deg,#e8edf2 0%,#d4dde6 50%,#bfcad6 100%)}

/* testimonials */
.testimonials{top:3170px;height:340px}
.testimonials h2{margin-top:30px}
.testimonials .lead{margin-top:12px}
.quotes{position:absolute;left:100px;top:130px;width:1000px;display:flex;justify-content:space-between}
.quote{width:310px;display:flex;gap:16px}
.avatar{flex:none;width:70px;height:70px;border-radius:50%;background:linear-gradient(135deg,#c7d3de,#8ea2b6)}
.quote h4{font-size:14px;font-weight:600;color:var(--deep)}
.quote .role{font-size:11px;color:var(--sky);margin-bottom:6px}
.quote p{font-size:12px;line-height:19px;color:var(--muted)}

/* footer */
.site-footer{top:3510px;height:326px;background:var(--navy);color:#b9c8da}
.footer-brand{position:absolute;left:100px;top:90px;display:flex;align-items:center;gap:12px}
.footer-brand .brand-dot{background:var(--white)}
.footer-brand .brand-name{color:var(--white)}
.footer-col{position:absolute;top:50px;font-size:12px;line-height:20px}
.footer-col h4{font-size:13px;font-weight:700;color:var(--white);margin-bottom:14px;letter-spacing:.5px}
.footer-col ul{list-style:none}
.footer-col li{line-height:20px}
.contact-row{display:flex;gap:10px;align-items:flex-start}
.contact-row svg{flex:none;margin-top:3px}
.footer-bar{position:absolute;left:0;top:272px;width:1200px;height:54px;border-top:1px solid #1d4576;display:flex;align-items:center;justify-content:space-between;padding:0 100px;font-size:11px}
.social{display:flex;align-items:center;gap:8px}
.social span.dot{width:18px;height:18px;border-radius:50%;background:#2a5a91}
</style>
</head>
<body>

<div class="section hero" role="img" aria-label="Photograph of business people in suits talking in a bright glass office lobby"></div>
<header class="section site-header">
  <div class="brand"><span class="brand-dot"></span><span class="brand-name">VORELTA</span></div>
  <nav class="main-nav"><span>HOME</span><span>ABOUT US</span><span>SERVICES</span><span>OFFER</span><span>TESTIMONIALS</span><span>CONTACT US</span></nav>
</header>
<div class="hero-text">
  <h1>WE ARE A</h1>
  <div class="tagline">wealth management consultancy</div>
  <p>we are working to earn money for our customers and make them your clients.</p>
  <a class="btn">Read more</a>
</div>
<svg class="hero-arrow" style="left:24px" viewBox="0 0 30 30"><path d="M19 6 L10 15 L19 24" fill="none" stroke="#ffffff" stroke-width="3"/></svg>
<svg class="hero-arrow" style="left:1146px" viewBox="0 0 30 30"><path d="M11 6 L20 15 L11 24" fill="none" stroke="#ffffff" stroke-width="3"/></svg>

<section class="section intro">
  <h2 class="section-title">We are a wealth management consultancy</h2>
  <p class="lead">We advise business owners and their families on every part of their wealth. Our fees are fixed and visible, and every commission we receive from insurers or builders is paid back to you. This keeps our advice independent and free from any conflict of interest, year after year.</p>
  <div class="services">
    <div class="service">
      <svg width="30" height="30" viewBox="0 0 30 30"><rect x="2" y="18" width="6" height="10" fill="#3176b5"/><rect x="12" y="11" width="6" height="17" fill="#3176b5"/><rect x="22" y="4" width="6" height="24" fill="#3176b5"/></svg>
      <div><h3>Wealth Planning</h3><p>We map your assets and goals, then build a long term plan that protects your family and your company.</p></div>
    </div>
    <div class="service">
      <svg width="30" height="30" viewBox="0 0 30 30"><circle cx="15" cy="10" r="6" fill="#3176b5"/><path d="M3 28 C3 19 27 19 27 28 Z" fill="#3176b5"/></svg>
      <div><h3>Wealth Management</h3><p>We follow your portfolio every day and adjust it with care, always choosing products on their merit alone.</p></div>
    </div>
    <div class="service">
      <svg width="30" height="30" viewBox="0 0 30 30"><rect x="4" y="3" width="22" height="24" rx="2" fill="#3176b5"/><rect x="8" y="7" width="14" height="5" fill="#ffffff"/><rect x="8" y="15" width="4" height="3" fill="#ffffff"/><rect x="13" y="15" width="4" height="3" fill="#ffffff"/><rect x="18" y="15" width="4" height="3" fill="#ffffff"/><rect x="8" y="20" width="4" height="3" fill="#ffffff"/><rect x="13" y="20" width="4" height="3" fill="#ffffff"/><rect x="18" y="20" width="4" height="3" fill="#ffffff"/></svg>
      <div><h3>Tax Planning</h3><p>We look at income, property and transfers together to keep your tax burden fair and fully within the law.</p></div>
    </div>
    <div class="service">
      <svg width="30" height="30" viewBox="0 0 30 30"><rect x="5" y="3" width="20" height="25" fill="#3176b5"/><rect x="9" y="8" width="12" height="2" fill="#ffffff"/><rect x="9" y="13" width="12" height="2" fill="#ffffff"/><rect x="9" y="18" width="8" height="2" fill="#ffffff"/></svg>
      <div><h3>Trust &amp; Corporate Services</h3><p>We set up and run the structures that hold your business, property and savings in a clean, simple way.</p></div>
    </div>
    <div class="service">
      <svg width="30" height="30" viewBox="0 0 30 30"><path d="M15 3 L28 12 L2 12 Z" fill="#3176b5"/><rect x="5" y="14" width="4" height="10" fill="#3176b5"/><rect x="13" y="14" width="4" height="10" fill="#3176b5"/><rect x="21" y="14" width="4" height="10" fill="#3176b5"/><rect x="2" y="25" width="26" height="3" fill="#3176b5"/></svg>
      <div><h3>Family Governance</h3><p>We help your family agree on clear rules for decisions, succession and the next generation of owners.</p></div>
    </div>
    <div class="service">
      <svg width="30" height="30" viewBox="0 0 30 30"><path d="M15 27 L4 16 C-1 10 6 2 11 7 L15 11 L19 7 C24 2 31 10 26 16 Z" fill="#3176b5"/></svg>
      <div><h3>Charity &amp; Philanthropy</h3><p>We guide your giving, from choosing causes to setting up a foundation that reflects the values you hold.</p></div>
    </div>
  </div>
</section>

<section class="section council">
  <h2 class="section-title">COUNCIL We offer the range of services under the family office</h2>
  <div class="cards">
    <div class="card" role="img" aria-label="Photograph of glass office towers against a blue sky" style="background:linear-gradient(180deg,#9fb4c8 0%,#5f7389 100%)">
      <span class="card-caption">Consulting a financial investment</span>
    </div>
    <div class="card" role="img" aria-label="Photograph of hands around a meeting table with papers" style="background:linear-gradient(160deg,#c9cfd6 0%,#8e8a86 100%)">
      <span class="card-caption">Insurance brokerage</span>
    </div>
    <div class="card" role="img" aria-label="Photograph of a hand holding a small model house" style="background:linear-gradient(160deg,#f2f3f5 0%,#c8ccd2 100%)">
      <span class="card-caption">Advising on real estate and unlisted companies</span>
    </div>
  </div>
  <div class="dots"><span class="on"></span><span></span><span></span></div>
</section>

<section class="section value">
  <div class="value-photo" role="img" aria-label="Photograph of a businessman in glasses working at a laptop"></div>
  <div class="value-panel">
    <h2>Our added value</h2>
    <p>Our ambition is to return the fees hidden inside financial products to our clients, so that the true price of advice is always clear and known.</p>
    <p>We bill a single annual fee based on your wealth. Nothing else. We are on your side, and only on your side.</p>
    <span class="btn-outline">Read more</span>
  </div>
</section>

<section class="section offer">
  <h2 class="section-title">Our service offer</h2>
  <p class="lead">We act as an independent family office that works in full compliance with the following values.</p>
  <div class="offer-list">
    <div class="offer-item">
      <svg width="90" height="90" viewBox="0 0 90 90"><line x1="45" y1="12" x2="45" y2="76" stroke="#0692cd" stroke-width="4"/><line x1="18" y1="24" x2="72" y2="24" stroke="#0692cd" stroke-width="4"/><path d="M8 50 L18 26 L28 50 Z" fill="none" stroke="#0692cd" stroke-width="3"/><path d="M62 50 L72 26 L82 50 Z" fill="none" stroke="#0692cd" stroke-width="3"/><rect x="30" y="74" width="30" height="5" fill="#0692cd"/></svg>
      <h3>The absence of conflict of interest</h3>
      <p>No commission ever drives our advice. What we receive from partners goes straight back to you.</p>
    </div>
    <div class="offer-item">
      <svg width="90" height="90" viewBox="0 0 90 90"><path d="M45 84 L45 46 L20 20 M45 46 L70 20 M45 46 L45 12" fill="none" stroke="#0692cd" stroke-width="6"/><path d="M12 12 L26 14 L14 26 Z M78 12 L64 14 L76 26 Z M45 2 L37 14 L53 14 Z" fill="#0692cd"/></svg>
      <h3>Non distribution of products</h3>
      <p>We sell no products of our own, so we can choose freely among the best on the market.</p>
    </div>
    <div class="offer-item">
      <svg width="90" height="90" viewBox="0 0 90 90"><rect x="16" y="16" width="46" height="62" fill="none" stroke="#0692cd" stroke-width="3"/><line x1="24" y1="30" x2="54" y2="30" stroke="#0692cd" stroke-width="3"/><line x1="24" y1="40" x2="54" y2="40" stroke="#0692cd" stroke-width="3"/><line x1="24" y1="50" x2="44" y2="50" stroke="#0692cd" stroke-width="3"/><path d="M74 10 L82 18 L52 62 L44 64 L46 56 Z" fill="#0692cd"/></svg>
      <h3>A fee based exclusively on fees</h3>
      <p>One clear annual fee, set as a share of your wealth and agreed with you in advance.</p>
    </div>
  </div>
</section>

<section class="section about">
  <div class="about-text">
    <h2>About Vorelta</h2>
    <p>Vorelta was founded to change the way business owners work with wealth managers and insurance brokers. We put transparency first, share every cost openly and build long relationships with families who want honest, independent advice on all their assets.</p>
    <a class="btn">Read more</a>
  </div>
  <div class="about-photo" role="img" aria-label="Photograph of a smiling businesswoman with folded arms in a bright office"></div>
</section>

<section class="section testimonials">
  <h2 class="section-title">Testimonials</h2>
  <p class="lead">Business owners across France share what working with an independent family office has changed for them.</p>
  <div class="quotes">
    <div class="quote"><div class="avatar" role="img" aria-label="Portrait of a client"></div><div><h4>Lucien Marot</h4><div class="role">Business owner</div><p>For the first time I know exactly what I pay for advice, and why.</p></div></div>
    <div class="quote"><div class="avatar" role="img" aria-label="Portrait of a client"></div><div><h4>Claire Dubreuil</h4><div class="role">Business owner</div><p>They found costs hidden in my contracts and gave every euro back to me.</p></div></div>
    <div class="quote"><div class="avatar" role="img" aria-label="Portrait of a client"></div><div><h4>Hugo Fontanel</h4><div class="role">Business owner</div><p>Clear answers, no sales pitch, and a plan my whole family understands.</p></div></div>
  </div>
</section>

<footer class="section site-footer">
  <div class="footer-brand"><span class="brand-dot"></span><span class="brand-name">VORELTA</span></div>
  <div class="footer-col" style="left:420px;width:230px">
    <h4>WHO WE ARE</h4>
    <p>Vorelta Family Office is an independent French firm serving business owners and their families with clear, fee based advice.</p>
    <p style="margin-top:10px;color:#ffffff">Read more</p>
  </div>
  <div class="footer-col" style="left:700px">
    <h4>WELCOME</h4>
    <ul><li>Home</li><li>About Us</li><li>Services</li><li>Offer</li><li>Testimonials</li><li>Contact Us</li></ul>
  </div>
  <div class="footer-col" style="left:880px;width:230px">
    <h4>CONTACT INFO</h4>
    <div class="contact-row"><svg width="12" height="14" viewBox="0 0 12 14"><path d="M6 0 C2.7 0 0 2.6 0 5.8 C0 10 6 14 6 14 C6 14 12 10 12 5.8 C12 2.6 9.3 0 6 0 Z" fill="#85acd3"/><circle cx="6" cy="5.8" r="2.2" fill="#0a2f5c"/></svg><span>14 avenue des Tilleuls<br>75008 Paris</span></div>
    <div class="contact-row" style="margin-top:8px"><svg width="12" height="12" viewBox="0 0 12 12"><path d="M2 0 L5 3 L3.5 4.5 C4.5 6.5 5.5 7.5 7.5 8.5 L9 7 L12 10 L10 12 C5 12 0 7 0 2 Z" fill="#85acd3"/></svg><span>+33 1 42 00 18 36</span></div>
    <div class="contact-row" style="margin-top:8px"><svg width="12" height="12" viewBox="0 0 12 12"><path d="M2 0 L5 3 L3.5 4.5 C4.5 6.5 5.5 7.5 7.5 8.5 L9 7 L12 10 L10 12 C5 12 0 7 0 2 Z" fill="#85acd3"/></svg><span>+33 1 42 00 18 37</span></div>
    <div class="contact-row" style="margin-top:8px"><svg width="12" height="10" viewBox="0 0 12 10"><rect x="0" y="0" width="12" height="10" fill="#85acd3"/><path d="M0 0 L6 5 L12 0" fill="none" stroke="#0a2f5c" stroke-width="1.2"/></svg><span>contact@vorelta-fo.fr</span></div>
  </div>
  <div class="footer-bar">
    <span>© 2015 Vorelta. All rights reserved.</span>
    <div class="social"><span>Connect with our social networks</span><span class="dot"></span><span class="dot"></span><span class="dot"></span><span class="dot"></span></div>
  </div>
</footer>

</body>
</html>
```